Package Storage Service

Ideas...

Business Name... "TUCK IT AT BRAMWOOD":
Store it,
Don’t Ship it;
4-LESS
Convenience, Quality, Service

Easy as ABC…
A. Contact Us 064-293-5527
B. We deliver
C. We pick-up & Store

LESS, is the new MORE

Box Size* (Approx) Weight Limit Price per Month
41 cm X 34 cm X 26 cm 10 Kilos 12 CHFs/per month
48 cm X 43 cm X 35 cm 25 Kilos 25 CHFs/per month

* Larger sizes and prices available upon request.

Contact: Tom /064-293-5527

These are only ideas for a small package storage service for local college students. The storage times are usually for 1 - 3 months.
I need a catchy, creative, colorful design for a new business.

This flyer will need to be printable in color. A-4 size or 8 1/2 " X 11".

Target Market(s)

Hotel Management students leaving their program for vacations for short terms. They return after vacation or after practical work experiences 4 study.

Industry/Entity Type

College

Requirements
Must have
• Prices, box sizes, catchy format.

Idea will forward to their address should they not return to the school; for a postage fee + 15.00 CHFs.

Contact information for the PICKUP and DELIVERY Service... see above.

Include a PICKUP AND DELIVERY Option in the flyer.
Nice to have
• Colorful boxes with a creative idea for someone to choose spending a little each month rather than a lot at one time. 25 CHFs rather than 125 CHFs.
Should not have
• Not too wordy.

```html
<!DOCTYPE html>
<html lang="en">
<head>
<meta charset="utf-8">
<title>Tuck It At Bramwood – Package Storage</title>
<link rel="stylesheet" href="https://fonts.googleapis.com/css2?family=Federo&family=Schoolbell&family=Didact+Gothic&display=swap">
<style>
  :root {
    --ink: #121212;
    --ink-soft: #3a3a3a;
    --white: #ffffff;
    --band: rgba(58, 58, 62, 0.62);
    --stripe-pink: #d9577a;
    --stripe-orange: #e9822c;
    --stripe-olive: #9da13a;
    --stripe-grey: #c9c6c4;
    --stripe-blue: #3d6fd1;
    --stripe-mint: #5fc9a8;
    --stripe-purple: #6e3a8e;
    --stripe-teal: #2f8f86;
    --cardboard: #d7a868;
    --cardboard-dark: #b98540;
  }
  * { margin: 0; padding: 0; box-sizing: border-box; }
  html, body { width: 1200px; height: 655px; overflow: hidden; }
  body { font-family: "Didact Gothic", sans-serif; color: var(--ink); }

  .flyer {
    position: relative;
    width: 1200px;
    height: 655px;
    overflow: hidden;
  }
  .fabric-backdrop {
    position: absolute;
    inset: 0;
    background: linear-gradient(90deg,
      var(--stripe-pink) 0%,
      var(--stripe-orange) 14%,
      var(--stripe-olive) 26%,
      var(--stripe-grey) 38%,
      var(--stripe-orange) 50%,
      var(--stripe-mint) 60%,
      var(--stripe-blue) 70%,
      var(--stripe-grey) 80%,
      var(--stripe-purple) 92%,
      var(--stripe-teal) 100%);
    opacity: 0.85;
  }

  .title-band {
    position: absolute;
    left: 170px;
    top: 118px;
    width: 866px;
    height: 148px;
    background: var(--band);
    text-align: center;
  }
  .business-name {
    margin-top: 34px;
    font-family: "Federo", sans-serif;
    font-size: 50px;
    letter-spacing: 3px;
    line-height: 1;
    color: var(--ink);
  }
  .tagline {
    margin-top: 24px;
    font-family: "Schoolbell", cursive;
    font-size: 22px;
    letter-spacing: 0.5px;
    color: var(--white);
  }

  .box-stack {
    position: absolute;
    left: 330px;
    top: 318px;
    width: 216px;
    height: 194px;
    background: linear-gradient(160deg, var(--cardboard) 30%, var(--cardboard-dark));
  }

  .steps {
    position: absolute;
    left: 563px;
    top: 318px;
  }
  .steps-heading {
    font-family: "Federo", sans-serif;
    font-size: 34px;
    line-height: 1;
    letter-spacing: 1px;
  }
  .step-list {
    list-style: none;
    font-family: "Federo", sans-serif;
    font-size: 23px;
    line-height: 22px;
    letter-spacing: 0.5px;
    text-shadow: 0.5px 0 0 var(--ink);
  }

  .price-table {
    margin-top: 10px;
    border-collapse: collapse;
    font-size: 14px;
    line-height: 14px;
    color: var(--ink-soft);
  }
  .price-table th, .price-table td {
    font-weight: normal;
    text-align: left;
    padding: 0 8px 0 0;
    white-space: nowrap;
  }
  .footnote {
    margin-top: 14px;
    font-size: 10.5px;
    font-style: italic;
    color: var(--ink-soft);
  }

  .contact-line {
    position: absolute;
    left: 0;
    right: 0;
    top: 632px;
    padding-left: 10px;
    text-align: center;
    font-family: "Federo", sans-serif;
    font-size: 14px;
    letter-spacing: 0.5px;
    text-shadow: 0.4px 0 0 var(--ink);
  }
</style>
</head>
<body>
<main class="flyer">
  <div class="fabric-backdrop" role="img" aria-label="Colourful vertical striped fabric background"></div>

  <header class="title-band">
    <h1 class="business-name">TUCK IT AT BRAMWOOD</h1>
    <p class="tagline">Store it, Don't Ship it; 4-LESS. Convenience, Quality, Service</p>
  </header>

  <div class="box-stack" role="img" aria-label="Stack of cardboard moving boxes"></div>

  <section class="steps">
    <h2 class="steps-heading">EASY AS ABC</h2>
    <ol class="step-list">
      <li>A. CONTACT US 064-293-5527</li>
      <li>B. WE DELIVER</li>
      <li>C. WE PICK-UP &amp; STORE</li>
    </ol>
    <table class="price-table">
      <tr><th>Box Size* (Approx)</th><th>Weight Limit</th><th>Price per Month</th></tr>
      <tr><td>41 cm X 34 cm X 26 cm</td><td>10 Kilos</td><td>12 CHFs/per month</td></tr>
      <tr><td>48 cm X 43 cm X 35 cm</td><td>25 Kilos</td><td>25 CHFs/per month</td></tr>
    </table>
    <p class="footnote">* Larger sizes and prices available upon request.</p>
  </section>

  <footer class="contact-line">CONTACT: TOM /064-293-5527</footer>
</main>
</body>
</html>
```